Price Trend Graphic for Estimates

I want to add a graphic to my estimates that shows the projected price trend of the work we are quoting to the customer. I have attached a couple ideas I was working on but they are garbage. Hopefully you can see the intent and make it look a lot better. Basically I want the customer to see a really a professional / technological graphic that will stimulate them to purchase Right Now! before the price goes up further. So maybe if the "Today's Price" looks nice and friendly and then becomes more critical and ominous as it goes forward 30 days.... 90 days.... Idea is to psychologically

Target Market(s)

Customers for our Construction business

Industry/Entity Type

Construction

Colors
0054AA
0677BA
7BADD7
CADEEF
E8F1F8
0094D4
00A9DD
6FCCEA
C7EBF8
E9F6FB
FFF300
FFF600
FEFA6F
FFFEC7
FFFEE8
F0912C
F2A743
F7CA91
FBE8D2
FDF5EE

Requirements
Must have
• nice looking graphic with upwards moving arrow and 3 price points
Nice to have
• technological / modern looking chart

```html
<!DOCTYPE html>
<html lang="en">
<head>
<meta charset="utf-8">
<title>Estimated Price Trend</title>
<link rel="stylesheet" href="https://fonts.googleapis.com/css2?family=Montserrat:wght@500;600;700;800&display=swap">
<style>
  :root {
    --page: #ffffff;
    --navy-deep: #0a1744;
    --navy: #0f2163;
    --navy-violet: #1b1a6e;
    --floor-blue: #0a4fb8;
    --axis: #39a6f0;
    --grid: rgba(110, 170, 255, 0.10);
    --line: #ffffff;
    --title-red: #e0321b;
    --title-white: #ffffff;
    --today: #22c33a;
    --day30: #f0912c;
    --day60: #e0321b;
    --price: #ffffff;
  }
  * { margin: 0; padding: 0; box-sizing: border-box; }
  html, body {
    width: 800px;
    height: 1200px;
    overflow: hidden;
    background: var(--page);
  }
  .canvas {
    position: relative;
    width: 800px;
    height: 1200px;
  }
  .trend-graphic {
    position: absolute;
    left: 0;
    top: 339px;
    width: 800px;
    height: 522px;
    display: block;
    font-family: "Montserrat", sans-serif;
  }
  .title-main { fill: var(--title-red); font-weight: 800; font-size: 31px; letter-spacing: 0.5px; }
  .title-sub { fill: var(--title-white); font-weight: 800; font-size: 31px; letter-spacing: 0.5px; }
  .point-label { font-weight: 600; font-size: 13px; text-anchor: middle; }
  .point-label.today { fill: var(--today); }
  .point-label.day30 { fill: var(--day30); }
  .point-label.day60 { fill: var(--day60); }
  .point-price { fill: var(--price); font-weight: 700; font-size: 20px; text-anchor: middle; letter-spacing: 0.5px; }
  .axis { stroke: var(--axis); stroke-width: 2; fill: none; }
  .trend-line { stroke: var(--line); stroke-width: 2.5; fill: none; stroke-linejoin: round; }
  .grid-line { stroke: var(--grid); stroke-width: 1; }
</style>
</head>
<body>
<main class="canvas">
  <svg class="trend-graphic" viewBox="0 0 800 522" xmlns="http://www.w3.org/2000/svg" role="img" aria-label="Estimated price trend chart rising from today to 60 days">
    <defs>
      <linearGradient id="bg-fill" x1="0" y1="0" x2="1" y2="1">
        <stop offset="0" stop-color="var(--navy-deep)"/>
        <stop offset="0.55" stop-color="var(--navy)"/>
        <stop offset="1" stop-color="var(--navy-violet)"/>
      </linearGradient>
      <linearGradient id="floor-glow" x1="0" y1="0" x2="0" y2="1">
        <stop offset="0" stop-color="var(--floor-blue)" stop-opacity="0"/>
        <stop offset="1" stop-color="var(--floor-blue)" stop-opacity="0.85"/>
      </linearGradient>
      <linearGradient id="bar-today" x1="0" y1="0" x2="0" y2="1">
        <stop offset="0" stop-color="#1fbf3a" stop-opacity="0.9"/>
        <stop offset="1" stop-color="#1fbf3a" stop-opacity="0"/>
      </linearGradient>
      <linearGradient id="bar-30" x1="0" y1="0" x2="0" y2="1">
        <stop offset="0" stop-color="#e07a2c" stop-opacity="0.85"/>
        <stop offset="1" stop-color="#e07a2c" stop-opacity="0"/>
      </linearGradient>
      <linearGradient id="bar-60" x1="0" y1="0" x2="0" y2="1">
        <stop offset="0" stop-color="#d42a22" stop-opacity="0.85"/>
        <stop offset="1" stop-color="#d42a22" stop-opacity="0"/>
      </linearGradient>
      <linearGradient id="arrow-fill" x1="0" y1="0" x2="1" y2="0">
        <stop offset="0" stop-color="#ffffff"/>
        <stop offset="0.5" stop-color="#f06a4a"/>
        <stop offset="1" stop-color="var(--day60)"/>
      </linearGradient>
      <radialGradient id="haze" cx="0.7" cy="0.5" r="0.5">
        <stop offset="0" stop-color="#3a4dd6" stop-opacity="0.35"/>
        <stop offset="1" stop-color="#3a4dd6" stop-opacity="0"/>
      </radialGradient>
    </defs>

    <!-- backdrop -->
    <rect class="backdrop" width="800" height="522" fill="url(#bg-fill)"/>
    <rect class="backdrop-haze" width="800" height="522" fill="url(#haze)"/>
    <rect class="floor-glow" y="380" width="800" height="142" fill="url(#floor-glow)"/>

    <!-- grid -->
    <g class="grid">
      <line class="grid-line" x1="0" y1="60" x2="800" y2="60"/>
      <line class="grid-line" x1="0" y1="105" x2="800" y2="105"/>
      <line class="grid-line" x1="0" y1="150" x2="800" y2="150"/>
      <line class="grid-line" x1="0" y1="195" x2="800" y2="195"/>
      <line class="grid-line" x1="0" y1="240" x2="800" y2="240"/>
      <line class="grid-line" x1="0" y1="285" x2="800" y2="285"/>
      <line class="grid-line" x1="0" y1="330" x2="800" y2="330"/>
      <line class="grid-line" x1="0" y1="375" x2="800" y2="375"/>
      <line class="grid-line" x1="0" y1="420" x2="800" y2="420"/>
      <line class="grid-line" x1="100" y1="0" x2="100" y2="484"/>
      <line class="grid-line" x1="160" y1="0" x2="160" y2="484"/>
      <line class="grid-line" x1="220" y1="0" x2="220" y2="484"/>
      <line class="grid-line" x1="280" y1="0" x2="280" y2="484"/>
      <line class="grid-line" x1="340" y1="0" x2="340" y2="484"/>
      <line class="grid-line" x1="400" y1="0" x2="400" y2="484"/>
      <line class="grid-line" x1="460" y1="0" x2="460" y2="484"/>
      <line class="grid-line" x1="520" y1="0" x2="520" y2="484"/>
      <line class="grid-line" x1="580" y1="0" x2="580" y2="484"/>
      <line class="grid-line" x1="640" y1="0" x2="640" y2="484"/>
      <line class="grid-line" x1="700" y1="0" x2="700" y2="484"/>
      <line class="grid-line" x1="760" y1="0" x2="760" y2="484"/>
    </g>

    <!-- price bars -->
    <rect class="bar bar-today" x="248" y="336" width="18" height="124" fill="url(#bar-today)"/>
    <rect class="bar bar-30" x="402" y="245" width="24" height="195" fill="url(#bar-30)"/>
    <rect class="bar bar-60" x="554" y="150" width="31" height="210" fill="url(#bar-60)"/>

    <!-- axes -->
    <g class="axes">
      <path class="axis" d="M48 61 H58 V484 H727 V474"/>
      <line class="axis" x1="48" y1="162" x2="58" y2="162"/>
      <line class="axis" x1="48" y1="246" x2="58" y2="246"/>
      <line class="axis" x1="48" y1="335" x2="58" y2="335"/>
      <line class="axis" x1="48" y1="436" x2="58" y2="436"/>
      <line class="axis" x1="136" y1="484" x2="136" y2="474"/>
      <line class="axis" x1="256" y1="484" x2="256" y2="474"/>
      <line class="axis" x1="413" y1="484" x2="413" y2="474"/>
      <line class="axis" x1="569" y1="484" x2="569" y2="474"/>
    </g>

    <!-- title -->
    <text class="title-main" x="82" y="81">ESTIMATED PRICE</text>
    <text class="title-sub" x="82" y="116">TREND</text>

    <!-- trend line and arrow -->
    <polyline class="trend-line" points="136,441 257,336 326,357 413,245 473,242 569,150"/>
    <polygon class="trend-arrow-shaft" points="569,147 692,96 694,101 571,153" fill="url(#arrow-fill)"/>
    <polygon class="trend-arrow-head" points="727,78 686,83 702,113" fill="var(--day60)"/>

    <!-- markers -->
    <g class="markers">
      <circle cx="136" cy="441" r="7" fill="#ffffff" stroke="#0f2163" stroke-width="2"/>
      <circle cx="136" cy="441" r="3.5" fill="#0f2163"/>
      <circle cx="326" cy="357" r="4" fill="#0f2163" stroke="#ffffff" stroke-width="1.5"/>
      <circle cx="473" cy="242" r="4" fill="#0f2163" stroke="#ffffff" stroke-width="1.5"/>
      <circle cx="257" cy="336" r="8" fill="#ffffff" stroke="var(--today)" stroke-width="3"/>
      <circle cx="413" cy="245" r="11" fill="#ffffff" stroke="var(--day30)" stroke-width="4"/>
      <circle cx="569" cy="150" r="14" fill="#ffffff" stroke="var(--day60)" stroke-width="5"/>
    </g>

    <!-- price points -->
    <text class="point-label today" x="259" y="293">TODAY</text>
    <text class="point-price" x="259" y="315">$6,500.00</text>
    <text class="point-label day30" x="413" y="197">30DAYS</text>
    <text class="point-price" x="413" y="220">$7,280.00</text>
    <text class="point-label day60" x="569" y="97">60DAYS</text>
    <text class="point-price" x="569" y="119">$7,460.00</text>
  </svg>
</main>
</body>
</html>
```